We are a Yacht Charter Broker servicing VIP clients on booking sailing catamarans and motor yacht...

We are looking for a wildly creative website to attract high net worth clients to work with us in booking their dream yacht vacation. A site that you think is 5 years ahead of its time. Sexy, modern and unique. Our company name is BRELLAVON. Our colors are navy blue and silver.
BLUE:
RGBB 0/44/92
CMYC 100/86/36/31
SILVER:
RGB 152/163/173
CMYK 43/29/25/0

HEX 98a3ad

Target Market(s)

High net worth people in need of white glove brokerage serving in finding and booking their dream yacht for a vacation of a lifetime.

Coding

Coded - Design and coding required

Number of Pages Required

1 page

Requirements
Must have
• Mobile friendly.
• Wildly creative and different. A website that we would expect to see 5 years from now.
• Pictures of yachts and or people on yachts. Palm tree landscapes.
• pictures of high end food related to the VIP yacht experience.
Nice to have
• Anything you feel would sell the yacht charter experience.
Should not have
• Nothing comes to mind.

```html
<!DOCTYPE html>
<html lang="en">
<head>
<meta charset="utf-8">
<title>Brellavon — Yacht Charter Brokerage</title>
<link rel="stylesheet" href="https://fonts.googleapis.com/css2?family=Cinzel:wght@400;600&family=Libre+Baskerville:wght@400&family=Lato:wght@400;700&display=swap">
<style>
:root{
  --navy:#1b3563;
  --navy-deep:#142a50;
  --silver:#98a3ad;
  --panel:#dcdcdc;
  --field-dark:#f1f1f1;
  --ink:#333a45;
  --muted:#6d7480;
  --white:#ffffff;
  --rule:#e3e3e3;
  --divider-dark:#8a9ab5;
  --divider-light:#6f86ad;
}
*{box-sizing:border-box;margin:0;padding:0}
html,body{width:1200px;height:5000px;overflow:hidden}
body{font-family:"Lato",Arial,sans-serif;color:var(--ink);background:var(--white);position:relative}
section,header,footer{position:absolute;left:0;width:1200px}
.btn{display:inline-block;font-size:14px;text-align:center;line-height:34px;height:38px;border-radius:3px}
.btn-outline-light{border:2px solid var(--white);color:var(--white)}
.btn-outline-navy{border:2px solid var(--navy);color:var(--navy)}
.section-title{font-family:"Libre Baskerville",Georgia,serif;font-weight:400;font-size:26px;letter-spacing:1px;color:var(--ink);text-align:center}
.centered{position:absolute;left:0;width:100%;text-align:center}
.divider{position:absolute;width:56px;height:12px;border-radius:2px;background:var(--divider-dark)}
.divider.on-navy{background:var(--divider-light)}

/* header */
.site-header{top:0;height:90px;background:var(--white);border-bottom:1px solid var(--rule)}
.brand{position:absolute;left:78px;top:18px;color:var(--navy)}
.brand-name{font-family:"Cinzel",Georgia,serif;font-size:30px;letter-spacing:5px;line-height:34px}
.brand-tag{font-size:8px;letter-spacing:3px;color:var(--silver);text-align:center;margin-top:2px}
.main-nav{position:absolute;right:72px;top:28px;display:flex;align-items:center;gap:26px;font-size:15px;color:var(--ink)}
.main-nav .book{background:var(--navy);color:var(--white);padding:0 16px;line-height:34px;height:34px}

/* hero */
.hero{top:90px;height:615px;background:linear-gradient(180deg,#4a7fb8 0%,#8fb7d9 38%,#3f7d8a 62%,#1f5a6e 100%)}
.hero-title{position:absolute;left:80px;top:178px;font-family:"Cinzel",Georgia,serif;font-weight:400;font-size:46px;color:var(--white);letter-spacing:1px}
.hero-copy{position:absolute;left:82px;top:245px;width:640px;font-size:15px;line-height:21px;color:var(--white)}
.hero .btn{position:absolute;left:82px;top:312px;width:152px}
.hero-notch{position:absolute;left:550px;bottom:0}

/* about + booking */
.intro{top:705px;height:602px}
.about{position:absolute;left:0;top:0;width:620px;height:602px;background:var(--panel)}
.about h2{position:absolute;left:80px;top:118px;font-family:"Libre Baskerville",Georgia,serif;font-weight:400;font-size:30px;color:var(--ink)}
.about p{position:absolute;left:80px;width:470px;font-size:14px;line-height:20px;color:var(--ink)}
.about .btn{position:absolute;left:80px;top:442px;width:152px}
.booking{position:absolute;left:620px;top:0;width:580px;height:602px;background:var(--navy)}
.booking h2{position:absolute;left:0;top:40px;width:100%;text-align:center;font-family:"Libre Baskerville",Georgia,serif;font-weight:400;font-size:30px;color:var(--white)}
.field{position:absolute;height:36px;background:var(--field-dark);border-radius:2px;font-size:13px;color:#777;padding:0 12px;line-height:36px;white-space:nowrap;overflow:hidden}
.field.select::after{content:"";position:absolute;right:12px;top:15px;border:5px solid transparent;border-top-color:#555}
.field.area{line-height:normal;padding-top:10px}
.booking .submit{position:absolute;left:63px;top:495px;width:434px;height:40px;background:var(--silver);color:var(--white);text-align:center;line-height:40px;font-size:15px;border-radius:2px}

/* features */
.features{top:1307px;height:610px;border-bottom:1px solid var(--rule)}
.feature{position:absolute;top:170px;width:300px;text-align:center}
.feature h3{margin-top:30px;font-family:"Libre Baskerville",Georgia,serif;font-weight:400;font-size:17px;color:var(--ink);letter-spacing:.5px}
.feature p{margin:26px auto 0;width:280px;font-size:14px;line-height:20px;color:var(--muted)}

/* yachts */
.yachts{top:1917px;height:960px}
.yacht-row{position:absolute;left:0;width:1200px;height:383px}
.yacht-text{position:absolute;top:0;width:600px;height:383px;background:var(--panel);text-align:center}
.yacht-text h3{margin-top:100px;font-family:"Libre Baskerville",Georgia,serif;font-weight:400;font-size:27px;color:var(--ink)}
.yacht-text p{margin:26px auto 0;width:400px;font-size:14px;line-height:20px;color:var(--ink)}
.yacht-photo{position:absolute;top:0;width:600px;height:383px}

/* destinations */
.destinations{top:2877px;height:616px;border-top:1px solid var(--rule)}
.dest-circle{position:absolute;top:186px;width:240px;height:240px;border-radius:50%}
.arrow{position:absolute}

/* testimonials */
.testimonials{top:3493px;height:440px;background:radial-gradient(ellipse at 50% 50%,#24427a 0%,#1b3563 70%)}
.testimonials .section-title{color:var(--white)}
.quote-text{position:absolute;left:240px;width:720px;top:195px;font-size:15px;line-height:22px;color:var(--white);text-align:center}
.client{position:absolute;left:0;width:100%;top:278px;text-align:center;color:var(--white);font-size:13px;line-height:17px}
.client-rule{position:absolute;left:435px;top:318px;width:330px;height:1px;background:var(--white)}

/* contact */
.contact{top:3933px;height:667px}
.contact .field{background:var(--panel);height:67px;line-height:67px;font-size:14px;color:#555;padding:0 18px}
.contact .field.area{line-height:normal;padding-top:20px}
.contact .btn{position:absolute;left:83px;top:560px;width:156px;height:42px;line-height:38px}

/* footer */
.site-footer{top:4600px;height:350px;background:var(--navy);color:var(--white)}
.foot-col{position:absolute;top:70px;font-size:14px;line-height:20px}
.foot-col h4{font-family:"Libre Baskerville",Georgia,serif;font-weight:400;font-size:17px;letter-spacing:.5px;margin-bottom:18px}
.foot-col ul{list-style:none}
.foot-col li{margin-bottom:8px}
.foot-col li.bullet::before{content:"•";margin-right:14px}
.contact-line{display:flex;align-items:center;gap:12px;margin-bottom:8px}
.newsletter-input{width:240px;height:34px;background:var(--field-dark);color:#666;font-size:13px;line-height:34px;padding:0 12px;margin-top:22px}
.newsletter-send{width:140px;height:34px;border:2px solid var(--white);text-align:center;line-height:30px;margin-top:14px}
.socials{display:flex;gap:22px;margin-top:26px}
.socials span{width:22px;height:22px;border-radius:50%;background:var(--white);display:block}
.bottom-bar{position:absolute;top:4950px;left:0;width:1200px;height:50px;font-size:13px;color:var(--ink);line-height:50px}
</style>
</head>
<body>

<header class="site-header">
  <div class="brand">
    <div class="brand-name">BRELLAVON</div>
    <div class="brand-tag">YACHT CHARTER BROKER</div>
  </div>
  <nav class="main-nav">
    <span>Charter a yacht</span><span>Services</span><span>Locations</span><span>About us</span><span>Contact us</span>
    <span class="book">Book a Yacht</span>
    <span>IN</span>
    <svg width="18" height="18" viewBox="0 0 18 18" aria-label="Search"><circle cx="7.5" cy="7.5" r="5.5" fill="none" stroke="#333a45" stroke-width="2"/><line x1="11.5" y1="11.5" x2="16.5" y2="16.5" stroke="#333a45" stroke-width="2.4"/></svg>
  </nav>
</header>

<section class="hero" role="img" aria-label="Guests standing on the bow of a white motor yacht on a blue sea, a palm-covered tropical island behind">
  <h1 class="hero-title">YACHT CHARTER BROKRAGE</h1>
  <p class="hero-copy">Lorem Ipsum is simply dummy text of the printing and typesetting industry.<br>Lorem Ipsum has been the industry's standard dummy text ever since the 1500s.</p>
  <span class="btn btn-outline-light">Read More</span>
  <svg class="hero-notch" width="100" height="32" viewBox="0 0 100 32" aria-hidden="true"><path d="M0 0 L100 0 L78 32 L22 32 Z" fill="#1b3563"/><polyline points="40,10 50,19 60,10" fill="none" stroke="#fff" stroke-width="2.5"/></svg>
</section>

<section class="intro">
  <div class="about">
    <h2>ABOUT US</h2>
    <div class="divider" style="left:80px;top:174px" role="img" aria-label="Small wave ornament"></div>
    <p style="top:245px">Lorem Ipsum is simply dummy text of the printing and typesetting industry. Lorem Ipsum has been the industry's standard dummy text ever since the 1500s, when an unknown printer took a galley of type and scrambled it to make a type specimen book.</p>
    <p style="top:338px">It has survived not only five centuries, but also the leap into electronic typesetting, remaining essentially unchanged.</p>
    <span class="btn btn-outline-navy">Read More</span>
  </div>
  <div class="booking">
    <h2>BOOK A YACHT</h2>
    <div class="divider on-navy" style="left:262px;top:98px" role="img" aria-label="Small wave ornament"></div>
    <div class="field" style="left:63px;top:135px;width:210px">Full name</div>
    <div class="field select" style="left:287px;top:135px;width:210px">Number of People</div>
    <div class="field select" style="left:63px;top:188px;width:210px">Dates From</div>
    <div class="field select" style="left:287px;top:188px;width:210px">Dates To</div>
    <div class="field select" style="left:63px;top:241px;width:434px">Yacht Type Intrested You in</div>
    <div class="field" style="left:63px;top:294px;width:210px">Email Address</div>
    <div class="field" style="left:287px;top:294px;width:210px">Phone Number</div>
    <div class="field area" style="left:63px;top:347px;width:434px;height:120px">Message</div>
    <div class="submit">Book a yacht</div>
  </div>
</section>

<section class="features">
  <h2 class="section-title centered" style="top:72px">WHY CHOOSE US</h2>
  <div class="divider" style="left:572px;top:122px" role="img" aria-label="Small wave ornament"></div>

  <div class="feature" style="left:117px">
    <svg width="150" height="150" viewBox="0 0 150 150" aria-hidden="true"><rect x="32" y="32" width="86" height="86" transform="rotate(45 75 75)" fill="none" stroke="#1b3563" stroke-width="2"/><rect x="52" y="68" width="6" height="22" fill="#1b3563"/><rect x="58" y="78" width="42" height="8" fill="#1b3563"/><rect x="94" y="80" width="6" height="12" fill="#1b3563"/><circle cx="66" cy="72" r="5" fill="#1b3563"/><rect x="73" y="68" width="26" height="9" rx="3" fill="#1b3563"/></svg>
    <h3>LUXURY CABINS</h3>
    <p>Lorem Ipsum is simply dummy text of the printing and typesetting industry. Lorem Ipsum has been the industry's standard dummy text ever since the 1500s.</p>
  </div>
  <div class="feature" style="left:450px">
    <svg width="150" height="150" viewBox="0 0 150 150" aria-hidden="true"><rect x="32" y="32" width="86" height="86" transform="rotate(45 75 75)" fill="none" stroke="#1b3563" stroke-width="2"/><polygon points="75,58 80,70 93,71 83,80 86,93 75,86 64,93 67,80 57,71 70,70" fill="#1b3563"/></svg>
    <h3>PROFESSIONAL CREW</h3>
    <p>Lorem Ipsum is simply dummy text of the printing and typesetting industry. Lorem Ipsum has been the industry's standard dummy text ever since the 1500s.</p>
  </div>
  <div class="feature" style="left:783px">
    <svg width="150" height="150" viewBox="0 0 150 150" aria-hidden="true"><rect x="32" y="32" width="86" height="86" transform="rotate(45 75 75)" fill="none" stroke="#1b3563" stroke-width="2"/><path d="M52 82 L98 82 L92 91 L58 91 Z" fill="#1b3563"/><path d="M62 82 L66 72 L86 72 L90 82 Z" fill="#1b3563"/><rect x="70" y="66" width="10" height="6" fill="#1b3563"/></svg>
    <h3>100 OF YACHTS</h3>
    <p>Lorem Ipsum is simply dummy text of the printing and typesetting industry. Lorem Ipsum has been the industry's standard dummy text ever since the 1500s.</p>
  </div>
</section>

<section class="yachts">
  <h2 class="section-title centered" style="top:56px">OUR YACHTS</h2>
  <div class="divider" style="left:572px;top:104px" role="img" aria-label="Small wave ornament"></div>

  <div class="yacht-row" style="top:176px">
    <div class="yacht-text" style="left:0">
      <h3>MOTOR YACHTS</h3>
      <p>Lorem Ipsum is simply dummy text of the printing and typesetting industry. Lorem Ipsum has been the industry's standard dummy text ever since the 1500s, when an unknown printer took a galley of type and scrambled it to make a type specimen book.</p>
    </div>
    <div class="yacht-photo" style="left:600px;background:radial-gradient(ellipse at 35% 45%,#4b86b3 0%,#1f5a8a 45%,#0f3a66 100%)" role="img" aria-label="Aerial view of a white motor yacht carving a curved wake across deep blue water"></div>
  </div>
  <div class="yacht-row" style="top:559px">
    <div class="yacht-photo" style="left:0;background:linear-gradient(180deg,#d7e6f2 0%,#6fa6d2 28%,#1f6aa3 45%,#0e4a80 100%)" role="img" aria-label="Several white sailing catamarans on a bright blue sea under a cloudy sky"></div>
    <div class="yacht-text" style="left:600px">
      <h3>SAILING CATAMARANS</h3>
      <p>Lorem Ipsum is simply dummy text of the printing and typesetting industry. Lorem Ipsum has been the industry's standard dummy text ever since the 1500s, when an unknown printer took a galley of type and scrambled it to make a type specimen book.</p>
    </div>
  </div>
</section>

<section class="destinations">
  <h2 class="section-title centered" style="top:66px">CHARTER DESTINATIONS</h2>
  <div class="divider" style="left:572px;top:116px" role="img" aria-label="Small wave ornament"></div>
  <svg class="arrow" style="left:58px;top:290px" width="20" height="40" viewBox="0 0 20 40" aria-hidden="true"><polyline points="16,2 4,20 16,38" fill="none" stroke="#c4c4c4" stroke-width="2"/></svg>
  <div class="dest-circle" style="left:163px;background:linear-gradient(180deg,#6fb0e0 0%,#9ac7a0 40%,#3f9a9c 70%,#2f7f8a 100%)" role="img" aria-label="Tropical bay with limestone cliffs, turquoise water and longtail boats"></div>
  <div class="dest-circle" style="left:480px;background:linear-gradient(180deg,#5d8fc4 0%,#7aa07a 35%,#c9684a 60%,#2d4f6e 100%)" role="img" aria-label="Colourful wooden harbour houses beneath green mountains"></div>
  <div class="dest-circle" style="left:797px;background:linear-gradient(180deg,#7fb1e0 0%,#b7a27c 45%,#6b8a5a 70%,#3f7a78 100%)" role="img" aria-label="Old stone bridge and town above a green river"></div>
  <svg class="arrow" style="left:1120px;top:290px" width="20" height="40" viewBox="0 0 20 40" aria-hidden="true"><polyline points="4,2 16,20 4,38" fill="none" stroke="#1b3563" stroke-width="2.5"/></svg>
  <span class="btn btn-outline-navy" style="position:absolute;left:527px;top:512px;width:146px">View All</span>
</section>

<section class="testimonials">
  <h2 class="section-title centered" style="top:70px">WHAT CLIENTS SAY</h2>
  <div class="divider on-navy" style="left:572px;top:118px" role="img" aria-label="Small wave ornament"></div>
  <svg style="position:absolute;left:586px;top:150px" width="28" height="24" viewBox="0 0 28 24" aria-hidden="true"><path d="M2 22 L2 12 Q2 2 12 2 L12 6 Q6 6 6 12 L12 12 L12 22 Z M16 22 L16 12 Q16 2 26 2 L26 6 Q20 6 20 12 L26 12 L26 22 Z" fill="#fff"/></svg>
  <svg class="arrow" style="left:56px;top:200px" width="20" height="44" viewBox="0 0 20 44" aria-hidden="true"><polyline points="16,2 4,22 16,42" fill="none" stroke="#fff" stroke-width="3"/></svg>
  <p class="quote-text">Lorem Ipsum is simply dummy text of the printing and typesetting industry. Lorem Ipsum has been the industry's standard dummy text ever since the 1500s, when an unknown printer took a galley of type and scrambled it to make a type specimen book.</p>
  <div class="client">JAMES HALE<br>(Client)</div>
  <div class="client-rule"></div>
  <svg class="arrow" style="left:1124px;top:200px" width="20" height="44" viewBox="0 0 20 44" aria-hidden="true"><polyline points="4,2 16,22 4,42" fill="none" stroke="#fff" stroke-width="3"/></svg>
  <span class="btn btn-outline-light" style="position:absolute;left:527px;top:356px;width:146px">View All</span>
</section>

<section class="contact">
  <h2 class="section-title centered" style="top:58px">GET IN TOUCH</h2>
  <div class="divider" style="left:572px;top:106px" role="img" aria-label="Small wave ornament"></div>
  <div class="field" style="left:83px;top:200px;width:327px">Full Name</div>
  <div class="field" style="left:433px;top:200px;width:330px">Email Address</div>
  <div class="field" style="left:787px;top:200px;width:330px">Phone Number</div>
  <div class="field area" style="left:83px;top:294px;width:1034px;height:233px">Message</div>
  <span class="btn btn-outline-navy">Send</span>
</section>

<footer class="site-footer">
  <div class="foot-col" style="left:83px;width:220px">
    <h4>ABOUT US</h4>
    <p>Lorem Ipsum is simply dummy text of the printing and typesetting industry. Lorem Ipsum has been the industry's standard dummy text.</p>
    <div class="socials" aria-label="Social links"><span></span><span></span><span></span><span></span></div>
  </div>
  <div class="foot-col" style="left:377px;width:260px">
    <h4>NEWSLETTER</h4>
    <p>Lorem Ipsum is simply dummy text of the printing.</p>
    <div class="newsletter-input">Email Address</div>
    <div class="newsletter-send">Send</div>
  </div>
  <div class="foot-col" style="left:690px;width:180px">
    <h4>QUICK LINKS</h4>
    <ul>
      <li class="bullet">Home</li><li class="bullet">Charter a yacht</li><li class="bullet">Locations</li><li class="bullet">About us</li><li class="bullet">Contact us</li>
    </ul>
  </div>
  <div class="foot-col" style="left:907px;width:260px">
    <h4>QUICK LINKS</h4>
    <div class="contact-line"><svg width="14" height="14" viewBox="0 0 14 14" aria-hidden="true"><path d="M3 1 L5 1 L6 4 L4.5 5.5 Q6 8.5 8.5 9.5 L10 8 L13 9 L13 11 Q13 13 11 13 Q1 12 1 3 Q1 1 3 1 Z" fill="#fff"/></svg>+012-345-6789</div>
    <div class="contact-line"><svg width="14" height="14" viewBox="0 0 14 14" aria-hidden="true"><rect x="1" y="2" width="12" height="10" fill="none" stroke="#fff" stroke-width="1.5"/><rect x="3" y="4" width="8" height="3" fill="#fff"/></svg>+012-345-6789</div>
    <div class="contact-line"><svg width="14" height="14" viewBox="0 0 14 14" aria-hidden="true"><rect x="1" y="3" width="12" height="9" fill="none" stroke="#fff" stroke-width="1.5"/><polyline points="1,3 7,8 13,3" fill="none" stroke="#fff" stroke-width="1.5"/></svg>info@brellavon.com</div>
    <div class="contact-line"><svg width="14" height="14" viewBox="0 0 14 14" aria-hidden="true"><path d="M7 13 Q2 7 2 5 A5 5 0 0 1 12 5 Q12 7 7 13 Z" fill="#fff"/><circle cx="7" cy="5" r="1.8" fill="#1b3563"/></svg>214 Harbor Quay Rd</div>
    <div style="padding-left:26px">Port Halden, MA 02110</div>
  </div>
</footer>

<div class="bottom-bar">
  <span style="position:absolute;left:83px">© Copyright 2018 Brellavon Yacht Charter Broker. All Right Reserved</span>
  <span style="position:absolute;right:83px">Privacy Policy · Terms &amp; Conditions</span>
</div>

</body>
</html>
```